Home Builder and Trade Supplier needs a Ad/leaflet/mail drop off leaflet design

HavenCrest is a business that builds homes, renovations, property maintenance and anything else construction related to residential homes. See photos I have attached that have a description of the business.

I'm after a double sided flyer for mail box drop offs. The market audience is up market expensive homes and offices. I have attached some examples of what i think would look good - I would like to see an example like or similar to that but by all means the designs you submit don't have to be a copy or similar. If you have something completely different in mind that you think would suit, please submit or even a rough draft if youre not sure I'll like it and you don't want to risk wasting time.

Please include the text and information in your designs that I have included in my examples.

Submissions before the 10 days are welcome and encouraged :)

Any questions, please feel free to ask on here or through email on: joram.k@mailvista.net

Pamphlet Size: 210 x 142mm (a quarter of an A4)
Double Sided Colour

Property Maintenance

Requirements
Must have
• Contact Us: 0412 958 601
www.havencresthomes.com.au
Double sided
Colour
Size: quater of an A4

```html
<!DOCTYPE html>
<html lang="en">
<head>
<meta charset="utf-8">
<title>HavenCrest – Quality Homes &amp; Trade Supplier</title>
<link href="https://fonts.googleapis.com/css2?family=Raleway:wght@300;400;500&family=Great+Vibes&display=swap" rel="stylesheet">
<style>
  :root {
    --orange: #f06a2c;
    --orange-column: #f47c44;
    --orange-soft: #fbc3a4;
    --footer-orange: #f15a24;
    --grey-band: #c9c9c9;
    --text-grey: #a8a8a8;
    --script-grey: #bdbdbd;
    --white: #ffffff;
  }
  * { margin: 0; padding: 0; box-sizing: border-box; }
  html, body { width: 846px; height: 1200px; overflow: hidden; background: var(--white); }
  .flyer {
    position: relative; width: 846px; height: 1200px; overflow: hidden;
    background: var(--white); font-family: 'Raleway', sans-serif;
  }
  .headline {
    position: absolute; left: 62px; top: 22px;
    color: var(--orange); font-weight: 400; font-size: 68px; line-height: 84px;
  }
  .headline .script {
    font-family: 'Great Vibes', cursive; color: var(--script-grey);
    font-size: 84px; margin-right: 8px;
  }
  .headline .line-two { display: block; margin-left: 44px; }

  .service-column {
    position: absolute; right: 0; background: var(--orange-column);
    width: 206px; list-style: none; padding-left: 24px;
  }
  .service-column.top { top: 0; height: 500px; padding-top: 64px; }
  .service-column.bottom { top: 830px; height: 160px; padding-top: 18px; }
  .service-column li {
    font-size: 20px; line-height: 31.2px; font-weight: 400; text-transform: uppercase;
    color: var(--white); letter-spacing: 0.2px;
  }
  .service-column li.soft { color: var(--orange-soft); }

  .photo { position: absolute; }
  .photo.pool { left: 0; top: 229px; width: 192px; height: 163px;
    background: linear-gradient(160deg, #b9b6c4 0%, #d9d3d6 45%, #6fa9c8 70%, #7b8a4c 100%); }
  .photo.basin { left: 206px; top: 229px; width: 210px; height: 163px;
    background: linear-gradient(180deg, #6d6d6d 0%, #9c9c9c 40%, #e6e6e6 70%, #f4f4f4 100%); }
  .photo.facade { left: 431px; top: 229px; width: 196px; height: 163px;
    background: linear-gradient(180deg, #f2f2f2 0%, #cfcfcf 40%, #5a5a5a 70%, #8e8a80 100%); }
  .photo.garden { left: 0; top: 518px; width: 846px; height: 312px;
    background: linear-gradient(100deg, #3e4a3a 0%, #7f8a5c 25%, #e9e6df 40%, #8b8f4a 55%, #a06a3c 75%, #6e4226 100%); }

  .body-copy {
    position: absolute; left: 60px; width: 555px;
    color: var(--text-grey); font-size: 16.5px; line-height: 20.5px; font-weight: 300;
  }
  .body-copy.intro { top: 417px; }
  .body-copy.contact { top: 851px; }

  .grey-band { position: absolute; left: 0; top: 990px; width: 846px; height: 16px; background: var(--grey-band); }
  .footer {
    position: absolute; left: 0; top: 1006px; width: 846px; height: 194px;
    background: var(--footer-orange); color: var(--white); text-align: center;
  }
  .footer .call-line { margin-top: 26px; font-size: 29px; font-weight: 400; letter-spacing: 1px; }
  .footer .phone { font-size: 80px; font-weight: 500; line-height: 78px; letter-spacing: 2px; }
  .footer .web { font-size: 28px; font-weight: 400; margin-top: 2px; }
</style>
</head>
<body>
<main class="flyer">
  <h1 class="headline"><span class="script">Quality</span>Homes<span class="line-two">&amp; Trade Supplier</span></h1>

  <ul class="service-column top">
    <li>New Homes</li><li class="soft">Maintenance</li><li>Electrical</li><li class="soft">Painting</li>
    <li>Tiling</li><li class="soft">Landscaping</li><li>Bricklaying</li><li class="soft">Fitouts</li>
    <li>Glazing</li><li class="soft">Roofing</li><li>Plumbing</li><li class="soft">Fencing</li>
    <li>Cleaning</li><li class="soft">Strata</li>
  </ul>

  <div class="photo pool" role="img" aria-label="Modern home courtyard with a lit swimming pool"></div>
  <div class="photo basin" role="img" aria-label="White bathroom basin with chrome tapware"></div>
  <div class="photo facade" role="img" aria-label="Contemporary multi-storey house facade at dusk"></div>

  <p class="body-copy intro">Experience the benefits of dealing with a local experienced engineer building your home. Other builders have many houses under construction simultaneously. We don’t. We believe in quality over quantity and build unique luxury houses.</p>

  <div class="photo garden" role="img" aria-label="Landscaped courtyard with lit feature wall, bamboo and timber fence"></div>

  <p class="body-copy contact">Contact HavenCrest to discuss building your new home. Our priority is ensuring your home is built smoothly and that the final result meets your expectations. Our experience allows us to deliver homes on time, on schedule, on budget and of exceeding quality. Please see our portfolio for current and past homes.</p>

  <ul class="service-column bottom">
    <li>Lawn Mowing</li><li class="soft">Engineering</li><li>Carpentry</li><li class="soft">Renovations</li>
  </ul>

  <div class="grey-band"></div>
  <footer class="footer">
    <p class="call-line">CONTACT US TODAY ON</p>
    <p class="phone">0412 958 601</p>
    <p class="web">www.havencresthomes.com.au</p>
  </footer>
</main>
</body>
</html>
```